依頼詳細
デザイン指示書を参考に居抜き物件をリフォームして開業を考えている人向けにデザインをしていただきたいと思います。
お客様の理想の店舗デザインを実現します。全体のイメージは、スタイリッシュでオシャレで、高級感のあるデザインを希望します。
サイトURL
ページ数
1ページ
希望イメージ
シンプル 複雑
単色 カラフル
暗い 明るい
日常 高級
遊び心 厳粛
未来的 伝統的
女性的 男性的
希望する色
茶系
納品ファイル
• 高解像度JPG (.jpg)
• イラストレーター形式 (.ai)
• フォトショップ形式 (.psd)
補足説明
レスポンシブデザインでお願い致します。指示書の中の事例画像は、現在準備中のため、ご提案をお願いします。
依頼金額を40000円に変更して、延長しました。
■ 選んだ理由

シンプルなデザインありがとうございました。

修正を引き続きよろしくお願いいたします。

■ 提案者全員のお礼・コメント

たくさんのデザインありがとうございました。
今後もデザインコンペを行ってまいりますのでよろしくお願い致します。

```html
<!DOCTYPE html>
<html lang="ja">
<head>
<meta charset="utf-8">
<title>店舗リフォームのミナト</title>
<link rel="stylesheet" href="https://fonts.googleapis.com/css2?family=Noto+Sans+JP:wght@400;500;700&family=Noto+Serif+JP:wght@500;700&display=swap">
<style>
:root{
  --brown:#6b4a2c;
  --gold:#b38b4d;
  --gold-light:#c9a46a;
  --beige:#f2ebdf;
  --beige-dark:#e6dac6;
  --text:#5a4a3a;
  --muted:#8a7b6a;
  --line:#dccfb9;
  --white:#ffffff;
  --dark:#55504a;
  --footer:#4a3a2c;
}
*{box-sizing:border-box;margin:0;padding:0}
html,body{width:1200px;height:3244px;overflow:hidden}
body{font-family:"Noto Sans JP",sans-serif;color:var(--text);background:var(--beige);position:relative;font-size:14px}
.abs{position:absolute}
/* header */
.site-header{left:0;top:0;width:1200px;height:124px;background:var(--white)}
.brand{left:50px;top:20px;display:flex;align-items:center;gap:12px}
.brand-mark{width:40px;height:40px;background:var(--brown)}
.brand-name{font-family:"Noto Serif JP",serif;font-weight:700;color:var(--brown);font-size:26px;line-height:1.1}
.brand-name small{display:block;font-size:15px;font-weight:700}
.header-contact{right:40px;top:22px;display:flex;align-items:center;gap:16px}
.header-contact .label{font-size:13px;color:var(--text)}
.tel{display:flex;align-items:center;gap:8px;font-size:30px;font-weight:700;color:var(--brown);letter-spacing:1px;white-space:nowrap}
.btn-mail{background:var(--gold);color:var(--white);display:flex;align-items:center;gap:8px;padding:0 20px;height:40px;font-size:14px;white-space:nowrap}
.global-nav{right:40px;top:92px;display:flex}
.global-nav a{color:var(--text);text-decoration:none;font-size:14px;padding:0 16px;border-left:1px solid var(--line)}
.global-nav a:first-child{border-left:none}
/* hero */
.hero{left:0;top:124px;width:1200px;height:526px;background:linear-gradient(90deg,#8d7f70,#c9bfb2 45%,#7a4a2e 75%,#a06a3c)}
.hero-catch{left:150px;top:110px;font-family:"Noto Serif JP",serif;font-size:32px;font-weight:700;color:var(--white);letter-spacing:2px;white-space:nowrap;z-index:2}
.circle{border-radius:50%;border:8px solid var(--white)}
.circle-before{left:430px;top:190px;width:300px;height:300px;background:radial-gradient(#d9cfc2,#9a8c7c)}
.circle-after{left:730px;top:110px;width:390px;height:390px;background:radial-gradient(#d44a2e,#6b2a1a)}
.tag{background:var(--gold);color:var(--white);font-size:14px;padding:4px 28px;border-radius:14px;white-space:nowrap}
/* cards */
.card{background:var(--white);border:1px solid var(--line)}
.card-title{display:flex;align-items:center;gap:12px;font-size:22px;font-weight:700;color:var(--brown);padding-bottom:12px;border-bottom:2px solid var(--line);margin-bottom:14px;white-space:nowrap}
.card-title .icon{width:24px;height:24px}
.card-title.light{font-weight:500;color:var(--muted)}
.body-text{font-size:14px;line-height:2;color:var(--text)}
.photo{background:linear-gradient(135deg,#cfc4b5,#8e8172)}
.btn-gold{background:var(--gold);color:var(--white);font-size:13px;display:flex;align-items:center;justify-content:center;gap:6px;white-space:nowrap}
.thumbs{display:grid;grid-template-columns:repeat(3,140px);gap:14px 16px}
.thumb .photo{height:78px}
.thumb p{font-size:11px;color:var(--muted);margin-top:4px}
.column-list li{list-style:none;font-size:12px;color:var(--muted);line-height:1.6;padding:8px 0;border-bottom:1px dotted var(--line)}
.section-title{display:flex;align-items:center;gap:14px;font-size:26px;font-weight:700;color:var(--muted);white-space:nowrap}
.news li{list-style:none;display:flex;gap:30px;font-size:13px;color:var(--text);padding:14px 20px;border-bottom:1px solid var(--line)}
.dark-btn{background:var(--dark);color:var(--white);font-size:18px;font-weight:700;display:flex;align-items:center;justify-content:space-between;padding:0 22px 0 64px;height:58px}
.footer{left:0;top:3000px;width:1200px;height:244px;background:var(--white)}
.footer-nav{display:flex;justify-content:center;margin-top:26px}
.footer-nav a{font-size:13px;color:var(--text);text-decoration:none;padding:0 12px;border-left:1px solid var(--line)}
.footer-nav a:first-child{border-left:none}
.copy{position:absolute;left:0;bottom:0;width:100%;height:40px;background:var(--footer);color:#d8cbb6;font-size:11px;text-align:center;line-height:40px}
</style>
</head>
<body>
<svg width="0" height="0" style="position:absolute">
  <symbol id="i-sq" viewBox="0 0 24 24"><rect x="0" y="0" width="24" height="6" fill="#6b4a2c"/><rect x="0" y="9" width="10" height="15" fill="#b38b4d"/><rect x="13" y="9" width="11" height="15" fill="#6b4a2c"/></symbol>
  <symbol id="i-phone" viewBox="0 0 24 24"><path d="M6 2l4 4-2 3c1 3 3 5 6 6l3-2 4 4-3 4C9 21 3 15 2 5z" fill="currentColor"/></symbol>
  <symbol id="i-mail" viewBox="0 0 24 24"><rect x="2" y="5" width="20" height="14" fill="none" stroke="currentColor" stroke-width="2"/><path d="M2 5l10 8 10-8" fill="none" stroke="currentColor" stroke-width="2"/></symbol>
  <symbol id="i-arrow" viewBox="0 0 12 12"><path d="M4 2l4 4-4 4" fill="none" stroke="currentColor" stroke-width="2"/></symbol>
  <symbol id="i-pin" viewBox="0 0 24 24"><path d="M12 2a7 7 0 0 1 7 7c0 5-7 13-7 13S5 14 5 9a7 7 0 0 1 7-7z" fill="currentColor"/><circle cx="12" cy="9" r="3" fill="#fff"/></symbol>
</svg>

<header class="site-header abs">
  <div class="brand abs"><span class="brand-mark"></span><div class="brand-name"><small>店舗リフォームの</small>ミナト</div></div>
  <div class="header-contact abs">
    <span class="label">お問い合わせ</span>
    <span class="tel"><svg width="26" height="26" style="color:var(--brown)"><use href="#i-phone"/></svg>000-555-0123</span>
    <span class="btn-mail"><svg width="18" height="18"><use href="#i-mail"/></svg>お問い合わせ</span>
  </div>
  <nav class="global-nav abs"><a href="#">HOME</a><a href="#">リフォームとは</a><a href="#">リフォーム工程</a><a href="#">事例紹介</a><a href="#">会社概要</a><a href="#">お問い合わせ</a></nav>
</header>

<section class="hero abs" role="img" aria-label="リフォーム後の美容室店舗の内装写真">
  <div class="circle circle-before abs" role="img" aria-label="リフォーム前の店内写真"></div>
  <div class="circle circle-after abs" role="img" aria-label="リフォーム後の和風飲食店の店内写真"></div>
  <p class="hero-catch abs">理想の店舗にリフォームいたします</p>
  <span class="tag abs" style="left:525px;top:484px">ビフォー</span>
  <span class="tag abs" style="left:870px;top:484px">アフター</span>
</section>

<section class="card abs" style="left:40px;top:704px;width:1120px;height:224px;padding:24px 28px">
  <h2 class="card-title" style="width:740px"><svg class="icon"><use href="#i-sq"/></svg>店舗リフォームのこだわり</h2>
  <p class="body-text" style="width:740px">こだわりテキストテキストテキストテキストテキストテキストテキストテキストテキストテキストテキストテキストテキストテキストテキストテキストテキストテキストテキストテキストテキストテキストテキストテキストテキストテキストテキストテキストテキストテキストテキストテキストテキストテキスト</p>
  <div class="photo abs" role="img" aria-label="店舗入口の写真" style="right:28px;top:24px;width:300px;height:170px"></div>
</section>

<section class="card abs" style="left:40px;top:944px;width:548px;height:224px;padding:24px 28px">
  <h2 class="card-title"><svg class="icon"><use href="#i-sq"/></svg>店舗リフォームの注意点</h2>
  <p class="body-text">注意点テキストテキストテキストテキストテキストテキストテキストテキストテキストテキストテキストテキストテキストテキストテキストテキストテキストテキスト</p>
</section>
<section class="card abs" style="left:612px;top:944px;width:548px;height:224px;padding:24px 28px">
  <h2 class="card-title"><svg class="icon"><use href="#i-sq"/></svg>店舗リフォームのアフターメンテナンス</h2>
  <p class="body-text">アフターメンテナンステキストテキストテキストテキストテキストテキストテキストテキストテキストテキストテキストテキストテキストテキストテキスト</p>
</section>

<section class="card abs" style="left:40px;top:1184px;width:548px;height:328px;padding:24px 28px">
  <h2 class="card-title light"><svg class="icon"><use href="#i-sq"/></svg>リフォーム施工事例</h2>
  <div class="thumbs">
    <div class="thumb"><div class="photo" role="img" aria-label="施工事例の写真"></div><p>リフォーム施工</p></div>
    <div class="thumb"><div class="photo" role="img" aria-label="施工事例の写真"></div><p>リフォーム施工</p></div>
    <div class="thumb"><div class="photo" role="img" aria-label="施工事例の写真"></div><p>リフォーム施工</p></div>
    <div class="thumb"><div class="photo" role="img" aria-label="施工事例の写真"></div><p>リフォーム施工</p></div>
    <div class="thumb"><div class="photo" role="img" aria-label="施工事例の写真"></div><p>リフォーム施工</p></div>
    <div class="thumb"><div class="photo" role="img" aria-label="施工事例の写真"></div><p>リフォーム施工</p></div>
  </div>
</section>
<section class="card abs" style="left:612px;top:1184px;width:548px;height:328px;padding:24px 28px">
  <h2 class="card-title light"><svg class="icon"><use href="#i-sq"/></svg>リフォームコラム</h2>
  <ul class="column-list">
    <li>2016/07/01<br>リフォーム施工の基本と注意点について解説します</li>
    <li>2016/07/01<br>居抜き物件を活かした店舗づくりのポイント紹介</li>
    <li>2016/07/01<br>リフォーム後のメンテナンスで長く使える店舗へ</li>
  </ul>
  <span class="btn-gold abs" style="left:160px;top:284px;width:230px;height:26px">一覧はこちら<svg width="10" height="10"><use href="#i-arrow"/></svg></span>
</section>

<h2 class="section-title abs" style="left:48px;top:1612px"><svg width="28" height="28"><use href="#i-sq"/></svg>店舗リフォームの施工事例</h2>
<div class="photo abs" role="img" aria-label="飲食店カウンターの施工事例写真" style="left:160px;top:1690px;width:428px;height:290px;background:linear-gradient(135deg,#b9ad9c,#6d5f4f)"></div>
<div class="photo abs" role="img" aria-label="カフェ客席の施工事例写真" style="left:612px;top:1690px;width:428px;height:290px;background:linear-gradient(135deg,#d6cfc4,#7f7466)"></div>
<div class="photo abs" role="img" aria-label="美容室の施工事例写真" style="left:160px;top:1994px;width:428px;height:290px;background:linear-gradient(135deg,#e8e6e2,#9c958c)"></div>
<div class="photo abs" role="img" aria-label="レストラン客席の施工事例写真" style="left:612px;top:1994px;width:428px;height:290px;background:linear-gradient(135deg,#c7b59b,#5e4630)"></div>
<span class="btn-gold abs" style="left:425px;top:2326px;width:350px;height:32px">施工事例一覧はこちら<svg width="10" height="10"><use href="#i-arrow"/></svg></span>

<section class="abs" style="left:40px;top:2436px;width:740px">
  <h2 class="section-title" style="color:var(--brown)"><svg width="28" height="28"><use href="#i-sq"/></svg>新着情報</h2>
  <span class="btn-gold abs" style="left:476px;top:4px;width:264px;height:30px">新着情報一覧を見る<svg width="10" height="10"><use href="#i-arrow"/></svg></span>
  <ul class="news" style="margin-top:28px">
    <li><span>2016/06/16</span><span>店舗リフォーム事例　架空町</span></li>
    <li><span>2016/06/16</span><span>店舗リフォーム事例　架空町</span></li>
    <li><span>2016/06/16</span><span>店舗リフォーム事例　架空町</span></li>
    <li><span>2016/06/16</span><span>店舗リフォーム事例　架空町</span></li>
  </ul>
</section>

<section class="card abs" style="left:800px;top:2420px;width:360px;height:200px;padding:18px 22px;border:2px solid var(--gold)">
  <h2 style="display:flex;align-items:center;gap:10px;font-size:22px;color:var(--brown)"><svg width="28" height="28" style="color:var(--gold)"><use href="#i-pin"/></svg>アクセス</h2>
  <p style="font-size:20px;font-weight:700;color:var(--brown);margin-top:8px">店舗リフォームのミナト</p>
  <p style="font-size:12px;line-height:1.7;color:var(--muted)">（有限会社ミナト建設）<br>〒100-0000<br>東京都架空区サンプル町1-2-3<br>TEL：000-555-0123</p>
  <span class="btn-gold abs" style="right:22px;bottom:16px;width:110px;height:24px">Mapを見る<svg width="10" height="10"><use href="#i-arrow"/></svg></span>
</section>
<div class="dark-btn abs" style="left:800px;top:2640px;width:360px">取り扱いメーカー<svg width="14" height="14"><use href="#i-arrow"/></svg></div>
<div class="dark-btn abs" style="left:800px;top:2750px;width:360px">加盟団体<svg width="14" height="14"><use href="#i-arrow"/></svg></div>

<section class="card abs" style="left:40px;top:2800px;width:740px;height:140px;display:flex;align-items:center;justify-content:center;gap:24px">
  <span style="font-size:13px">お問い合わせ</span>
  <div style="text-align:center">
    <p style="font-size:18px;font-weight:700;color:var(--brown)">お気軽にお問い合わせください</p>
    <span class="tel"><svg width="26" height="26" style="color:var(--brown)"><use href="#i-phone"/></svg>000-555-0123</span>
  </div>
  <span class="btn-mail"><svg width="18" height="18"><use href="#i-mail"/></svg>お問い合わせ</span>
</section>

<footer class="footer abs">
  <nav class="footer-nav"><a href="#">HOME</a><a href="#">リフォームとは</a><a href="#">リフォーム工程</a><a href="#">事例紹介</a><a href="#">会社概要</a><a href="#">お問い合わせ</a></nav>
  <p style="text-align:center;font-family:'Noto Serif JP',serif;font-weight:700;font-size:22px;color:var(--brown);margin-top:24px">店舗リフォームのミナト</p>
  <p style="text-align:center;font-size:12px;color:var(--muted);margin-top:6px">〒100-0000 東京都架空区サンプル町1-2-3　TEL：000-555-0123</p>
  <div class="copy">Copyright(c) 店舗リフォームのミナト All Rights Reserved.</div>
</footer>
</body>
</html>
```